Book Cover Design Project

I need a book cover design with the title

"Gilded Ledger - A Probe into Avarice and Graft in Australia’s $1 Trillion Retirement Savings Sector"

With a question on the cover of "How much of your superannuation has been stolen? Read this Book to Find Out"

The design should have money and greed based theme such as "$" for "S" in "Super"

Target Market(s)

Members of Superannuation (Pension) funds

Industry/Entity Type

Industry

Requirements
Must have
• Must have a money and greed theme

```html
<!DOCTYPE html>
<html lang="en">
<head>
<meta charset="utf-8">
<title>Gilded Ledger – Book Cover</title>
<link rel="stylesheet" href="https://fonts.googleapis.com/css2?family=Archivo:wght@400;700;800;900&family=Roboto:wght@300;400;700&family=Source+Serif+4:ital,wght@0,400;0,600;1,400&display=swap">
<style>
  :root {
    --page-bg: #f2f2f2;
    --cover-bg: #ffffff;
    --cover-edge: #dcdcdc;
    --title-red: #d7262e;
    --ink-grey: #8a8a8a;
    --ink-dark: #5e5e5e;
    --ghost-grey: #ececec;
    --tab-grey: #9c9c9c;
    --tab-ink: #ffffff;
  }
  * { box-sizing: border-box; margin: 0; padding: 0; }
  html, body {
    width: 1200px; height: 900px; overflow: hidden;
    background: var(--page-bg);
  }
  .cover {
    position: absolute; left: 290px; top: 20px;
    width: 620px; height: 860px;
    background: var(--cover-bg);
    border: 1px solid var(--cover-edge);
    overflow: hidden;
    font-family: "Roboto", Arial, sans-serif;
  }
  .cover__ghost-dollar {
    position: absolute; right: -150px; top: 120px;
    font-family: "Archivo", Arial, sans-serif; font-weight: 900;
    font-size: 820px; line-height: 1;
    color: var(--ghost-grey);
    user-select: none;
  }
  .cover__question {
    position: absolute; left: 38px; top: 30px;
    font-size: 13px; color: var(--ink-grey); letter-spacing: .2px;
  }
  .cover__title {
    position: absolute; left: 34px; top: 58px;
    font-family: "Archivo", Arial, sans-serif; font-weight: 800;
    font-size: 108px; line-height: .92; letter-spacing: -2px;
    color: var(--title-red);
    text-transform: uppercase;
  }
  .cover__title span { display: block; }
  .cover__byline {
    position: absolute; left: 36px; top: 282px;
    font-family: "Archivo", Arial, sans-serif; font-weight: 800;
    font-size: 40px; letter-spacing: -1px;
    color: var(--ink-grey); text-transform: uppercase;
    white-space: nowrap;
  }
  .cover__subtitle {
    position: absolute; left: 340px; top: 340px; width: 260px;
    color: var(--ink-grey); font-size: 17px; line-height: 1.1;
  }
  .cover__subtitle strong {
    display: block; font-family: "Archivo", Arial, sans-serif;
    font-weight: 800; font-size: 40px; line-height: 1; color: var(--ink-dark);
    letter-spacing: -1px;
  }
  .definition {
    position: absolute; left: 36px; top: 520px; width: 360px;
    font-family: "Source Serif 4", Georgia, serif;
    font-size: 10.5px; line-height: 1.45; color: var(--ink-grey);
  }
  .definition__tab {
    width: 46px; height: 46px; background: var(--tab-grey);
    color: var(--tab-ink); font-family: "Archivo", Arial, sans-serif;
    font-weight: 700; font-size: 30px; line-height: 46px; text-align: center;
    margin-bottom: 14px;
  }
  .definition__head { margin-left: 22px; margin-bottom: 16px; }
  .definition__pos { margin-left: 22px; margin-bottom: 14px; }
  .definition__meaning { margin-bottom: 12px; }
  .definition__list { margin-left: 14px; margin-bottom: 16px; }
  .definition__origin-label { font-weight: 600; margin-bottom: 12px; }
</style>
</head>
<body>
  <main class="cover">
    <div class="cover__ghost-dollar" aria-hidden="true">$</div>

    <p class="cover__question">How much of your superannuation has been stolen? Read this book to find out.</p>

    <h1 class="cover__title">
      <span>Gilded</span>
      <span>Ledger</span>
    </h1>

    <p class="cover__byline">By ‘Authors Name’</p>

    <p class="cover__subtitle">
      a probe into avarice<br>
      &amp; graft in Australia’s
      <strong>$1 trillion</strong>
      retirement savings sector
    </p>

    <section class="definition">
      <div class="definition__tab">G</div>
      <p class="definition__head">Definition of graft</p>
      <p class="definition__pos">noun<br>[mass noun]</p>
      <p class="definition__meaning">practices, especially bribery, used to secure illicit gains in politics or business; corruption</p>
      <ul class="definition__list">
        <li>[count noun] a bribe or illicit payment made to obtain favour</li>
        <li>money taken dishonestly from members’ savings</li>
      </ul>
      <p class="definition__origin-label">Origin:</p>
      <p>Mid 19th century: of unknown origin, perhaps from an older sense of ‘dig’</p>
    </section>
  </main>
</body>
</html>
```